User Interface Designer Needed

I need a few designs for a property law comparison website. We assist the public with finding a solicitor for the purchase or sale of their house and units. We are currently in the process of creating a questionnaire based woo commerce product filter using gravity forms. I'd like to see designs that use the logo colours. Users will be selecting options such as "Buying" or "Selling", they will then be selecting options such as "House" "Unit" or "Land". Details attached. The final design should communicate ease and simplicity. Questions will be answered one at a time, and the next question is dependent on the answer to the question prior

Target Market(s)

First home buyers, people from ages 18-80 make and female looking to get rid of the hassle of ringing around and going from website to website trying to get a quote

Industry/Entity Type

Real Estate

Number of Pages Required

1 page

Colors
33a6d7

Requirements
Must have
• A design for every question
Nice to have
• Simple symbols or simplistic pictures incorporated, even better if you can turn the question into a picture instead of words eg. A picture of a house, a picture of a unit and a picture of land instead of written answers

```html
<!DOCTYPE html>
<html lang="en">
<head>
<meta charset="utf-8">
<title>Parcelo – Filter / Question</title>
<link href="https://fonts.googleapis.com/css2?family=Open+Sans:wght@300;400;600;700&display=swap" rel="stylesheet">
<style>
:root{
  --brand:#33a6d7;
  --brand-dark:#1e8fc2;
  --orange:#f39a12;
  --orange-dark:#e2850a;
  --ink:#3d3d3d;
  --muted:#6f6f6f;
  --panel:#efefef;
  --panel-border:#dedede;
  --line:#e3e3e3;
  --footer:#2f2f2f;
  --footer-bottom:#262626;
  --footer-text:#e6e6e6;
  --footer-muted:#6b6b6b;
}
*{box-sizing:border-box;margin:0;padding:0}
html,body{width:1200px;height:2200px;overflow:hidden}
body{position:relative;background:#fff;font-family:'Open Sans',Arial,sans-serif;color:var(--ink);border-top:3px solid var(--brand)}

/* header */
.site-header{position:absolute;top:3px;left:0;width:1200px;height:114px;background:#fff;border-bottom:1px solid var(--line)}
.brand{position:absolute;left:98px;top:26px;display:flex;align-items:center;gap:12px;font-size:40px;font-weight:600;color:#4a4a4a;letter-spacing:-0.5px}
.brand-dot{width:44px;height:44px;border-radius:50%;background:var(--brand)}
.search{position:absolute;left:780px;top:37px;display:flex}
.search-input{width:242px;height:34px;border:1px solid #dcdcdc;border-right:none;font-size:12px;color:#9a9a9a;padding:0 10px;display:flex;align-items:center}
.search-btn{width:38px;height:34px;background:var(--brand);display:flex;align-items:center;justify-content:center}
.menu-toggle{position:absolute;left:1076px;top:44px;width:24px;height:20px;display:flex;flex-direction:column;justify-content:space-between}
.menu-toggle span{display:block;height:4px;background:#6a6a6a;border-radius:1px}

/* hero */
.hero{position:absolute;top:117px;left:0;width:1200px;height:420px;background:linear-gradient(180deg,#5ea9e4 0%,#a9d0ef 38%,#b9b2a2 55%,#7f8f63 72%,#5f8f35 100%)}
.hero-banner{position:absolute;left:98px;top:147px;width:619px;height:122px;background:rgba(51,166,215,.88);padding:7px}
.hero-banner-inner{width:100%;height:100%;border:1px solid rgba(255,255,255,.55);display:flex;align-items:center;padding-left:24px;gap:18px}
.hero-mark{width:62px;height:62px;border-radius:50%;border:6px solid #fff}
.hero-title{font-size:32px;color:#fff;letter-spacing:.5px;font-weight:300}
.hero-title strong{font-weight:700}
.hero-dots{position:absolute;left:1029px;top:365px;display:flex;gap:13px}
.hero-dots span{width:16px;height:16px;border-radius:50%;background:#fff}
.hero-dots span.is-active{background:var(--brand);box-shadow:0 0 0 2px #fff}

/* filter */
.filter{position:absolute;top:567px;left:98px;width:1002px}
.filter-heading{display:flex;align-items:center;gap:10px;color:var(--brand);font-size:22px;font-weight:400;margin-bottom:26px}
.question{background:var(--panel);border:1px solid var(--panel-border);border-radius:3px;padding:26px 30px 18px 17px;margin-bottom:25px}
.question.no-title{padding-top:24px}
.question-title{display:flex;align-items:center;gap:10px;height:24px;margin-bottom:14px;font-size:16px;color:#4a4a4a}
.question-icon{width:26px;height:26px;border-radius:50%;border:3px solid var(--brand)}
.option{display:flex;align-items:center;gap:10px;height:29px;padding-left:15px;font-size:10px;font-weight:600;text-transform:uppercase;letter-spacing:.3px;color:var(--muted)}
.box{width:14px;height:14px;border:1px solid #d2d2d2;border-radius:2px;background:#e4e4e4;display:flex;align-items:center;justify-content:center}
.option.is-checked .box{background:var(--brand);border-color:var(--brand-dark)}

.actions{display:flex;justify-content:space-between;margin-top:16px}
.actions-group{display:flex;gap:9px}
.btn{height:39px;display:flex;align-items:center;justify-content:center;gap:6px;font-size:12px;font-weight:600;text-transform:uppercase;border-radius:3px}
.btn-ghost{width:103px;background:linear-gradient(#fafafa,#e6e6e6);border:1px solid #d3d3d3;color:var(--brand)}
.btn-edit{width:103px;background:linear-gradient(#f7a622,var(--orange-dark));color:#fff}
.btn-done{width:102px;background:linear-gradient(#3cb2e2,var(--brand-dark));color:#fff}

/* footer */
.site-footer{position:absolute;left:0;top:2010px;width:1200px;height:139px;background:var(--footer)}
.footer-col{position:absolute;top:40px}
.footer-label{font-size:11px;font-weight:700;color:#fff;text-transform:uppercase;letter-spacing:.3px;margin-bottom:8px}
.footer-value{font-size:17px;color:var(--footer-text)}
.footer-divider{position:absolute;top:34px;width:1px;height:76px;background:#474747}
.social{display:flex;gap:11px;margin-top:4px}
.social span{width:25px;height:25px;border-radius:3px;background:#8fa9c8}
.subscribe{display:flex;margin-top:2px}
.subscribe-input{width:179px;height:32px;background:#fff;font-size:10px;color:#a0a0a0;display:flex;align-items:center;padding-left:12px}
.subscribe-btn{width:73px;height:32px;background:var(--brand);color:#fff;font-size:11px;display:flex;align-items:center;justify-content:center}
.footer-bottom{position:absolute;left:0;top:2149px;width:1200px;height:51px;background:var(--footer-bottom);display:flex;align-items:center;justify-content:center;gap:10px;font-size:11px;color:var(--footer-muted);text-transform:uppercase}
.footer-bottom-dot{width:22px;height:22px;border-radius:50%;border:2px solid var(--footer-muted)}
</style>
</head>
<body>

<header class="site-header">
  <div class="brand"><span class="brand-dot"></span>Parcelo.com.au</div>
  <div class="search">
    <div class="search-input">Search</div>
    <div class="search-btn">
      <svg width="13" height="13" viewBox="0 0 14 14"><circle cx="6" cy="6" r="4.2" fill="none" stroke="#fff" stroke-width="2"/><line x1="9" y1="9" x2="12.5" y2="12.5" stroke="#fff" stroke-width="2" stroke-linecap="round"/></svg>
    </div>
  </div>
  <div class="menu-toggle"><span></span><span></span><span></span></div>
</header>

<section class="hero" role="img" aria-label="Photo of a large two-storey family home with a green lawn and blue sky">
  <div class="hero-banner">
    <div class="hero-banner-inner">
      <span class="hero-mark"></span>
      <h1 class="hero-title"><strong>ACCUSANTIUM</strong> DOLOREMQUE</h1>
    </div>
  </div>
  <div class="hero-dots"><span class="is-active"></span><span></span><span></span></div>
</section>

<main class="filter">
  <h2 class="filter-heading">
    <svg width="17" height="17" viewBox="0 0 16 16"><path d="M0 1h16L10 8v7l-4-2V8z" fill="currentColor"/></svg>
    FILTER/QUESTION
  </h2>

  <div class="question">
    <div class="question-title"><span class="question-icon"></span>I am a</div>
    <div class="option is-checked"><span class="box"><svg width="10" height="10" viewBox="0 0 10 10"><path d="M1.5 5.2l2.3 2.3 4.7-5" fill="none" stroke="#fff" stroke-width="1.6"/></svg></span>Buyer</div>
    <div class="option"><span class="box"></span>Seller</div>
    <div class="option"><span class="box"></span>Buyer and seller land</div>
  </div>

  <div class="question">
    <div class="question-title"><span class="question-icon"></span>I am a I'm buying a</div>
    <div class="option is-checked"><span class="box"><svg width="10" height="10" viewBox="0 0 10 10"><path d="M1.5 5.2l2.3 2.3 4.7-5" fill="none" stroke="#fff" stroke-width="1.6"/></svg></span>House</div>
    <div class="option"><span class="box"></span>Unit</div>
    <div class="option"><span class="box"></span>Land</div>
    <div class="option"><span class="box"></span>House and land package</div>
  </div>

  <div class="question">
    <div class="question-title"><span class="question-icon"></span>I would like</div>
    <div class="option is-checked"><span class="box"><svg width="10" height="10" viewBox="0 0 10 10"><path d="M1.5 5.2l2.3 2.3 4.7-5" fill="none" stroke="#fff" stroke-width="1.6"/></svg></span>Only the searches I need</div>
    <div class="option"><span class="box"></span>Standard searches</div>
    <div class="option"><span class="box"></span>Premium searches</div>
    <div class="option"><span class="box"></span>I don't need searches included in my quote – I'll pay for searches later at cost</div>
  </div>

  <div class="question">
    <div class="question-title"><span class="question-icon"></span>I would like</div>
    <div class="option is-checked"><span class="box"><svg width="10" height="10" viewBox="0 0 10 10"><path d="M1.5 5.2l2.3 2.3 4.7-5" fill="none" stroke="#fff" stroke-width="1.6"/></svg></span>Only the searches I need</div>
    <div class="option"><span class="box"></span>Standard searches</div>
    <div class="option"><span class="box"></span>Premium searches</div>
    <div class="option"><span class="box"></span>I don't need searches included in my quote – I'll pay for searches later at cost</div>
  </div>

  <div class="question no-title">
    <div class="option is-checked"><span class="box"><svg width="10" height="10" viewBox="0 0 10 10"><path d="M1.5 5.2l2.3 2.3 4.7-5" fill="none" stroke="#fff" stroke-width="1.6"/></svg></span>I want my quote to include unlimited extensions</div>
    <div class="option"><span class="box"></span>I only want to pay for extensions if I need them</div>
  </div>

  <div class="question no-title">
    <div class="option is-checked"><span class="box"><svg width="10" height="10" viewBox="0 0 10 10"><path d="M1.5 5.2l2.3 2.3 4.7-5" fill="none" stroke="#fff" stroke-width="1.6"/></svg></span>I have signed a contract</div>
    <div class="option"><span class="box"></span>I haven't signed a contract yet</div>
  </div>

  <div class="question no-title">
    <div class="option is-checked"><span class="box"><svg width="10" height="10" viewBox="0 0 10 10"><path d="M1.5 5.2l2.3 2.3 4.7-5" fill="none" stroke="#fff" stroke-width="1.6"/></svg></span>Risk</div>
    <div class="option"><span class="box"></span>I want my quote to allow for the possibility of</div>
    <div class="option"><span class="box"></span>Terminations</div>
    <div class="option"><span class="box"></span>Deed of recissions</div>
    <div class="option"><span class="box"></span>Deed of variations</div>
  </div>

  <div class="actions">
    <div class="actions-group">
      <div class="btn btn-ghost">« Preview</div>
      <div class="btn btn-ghost">Next »</div>
    </div>
    <div class="actions-group">
      <div class="btn btn-edit">Edit
        <svg width="12" height="12" viewBox="0 0 12 12"><rect x="1" y="2" width="8" height="9" fill="none" stroke="#fff" stroke-width="1.3"/><path d="M5 7l5.5-5.5" stroke="#fff" stroke-width="1.6"/></svg>
      </div>
      <div class="btn btn-done">Done
        <svg width="12" height="12" viewBox="0 0 12 12"><path d="M1 5h2.5v6H1zM4.5 5l2-4c1 0 1.5.6 1.3 1.6L7.5 4.5H11l-1 6.5H4.5z" fill="none" stroke="#fff" stroke-width="1.1"/></svg>
      </div>
    </div>
  </div>
</main>

<footer class="site-footer">
  <div class="footer-col" style="left:98px">
    <div class="footer-label">Address</div>
    <div class="footer-value">418 Harbour Lane, Bayview, NSW</div>
  </div>
  <span class="footer-divider" style="left:443px"></span>
  <div class="footer-col" style="left:463px">
    <div class="footer-label">Phone</div>
    <div class="footer-value">555.010.4821</div>
  </div>
  <span class="footer-divider" style="left:598px"></span>
  <div class="footer-col" style="left:626px">
    <div class="footer-label">Follow us on :</div>
    <div class="social"><span></span><span></span><span></span><span></span><span style="background:#e8e8e8"></span></div>
  </div>
  <span class="footer-divider" style="left:824px"></span>
  <div class="footer-col" style="left:848px">
    <div class="footer-label">Newsletter subscribe</div>
    <div class="subscribe">
      <div class="subscribe-input">Email Address</div>
      <div class="subscribe-btn">Subscribe</div>
    </div>
  </div>
</footer>
<div class="footer-bottom"><span class="footer-bottom-dot"></span>Copyrights©parcelo.com.2016 | Allrights reserved.</div>

</body>
</html>
```